Business card design for event company

need design double sided in square shape ( approx 6x6cm) in matt grey shades
front side :
logo ( could be in one color like picture attached ) printpress effect in a rect box

back side :
name in big font with silver foil finish ( similar to attached pic )

phone number i would like to see how it will look like if embossed ( like in credit cards )

Sample for contact on card ( will need 5 different contacts) - pls. include small icons next to each contact

WALEED RAFIQI
Managing Director

+971 50 317 6490
waleed@loomcrestuae.com
www.loomcrest.ae
Building C2 , Office 713
Dubai Saffron Heights

Please consider this is an urgent project . thank you in advance

```html
<!DOCTYPE html>
<html lang="en">
<head>
<meta charset="utf-8">
<title>Loomcrest Business Card</title>
<link rel="stylesheet" href="https://fonts.googleapis.com/css2?family=Oswald:wght@500&family=Roboto+Condensed:wght@400;500&display=swap">
<style>
  :root {
    --page: #dedede;
    --card: #1f1f1f;
    --card-light: #2c2c2c;
    --accent: #f0921f;
    --ink: #ffffff;
  }
  * { margin: 0; padding: 0; box-sizing: border-box; }
  html, body { width: 1200px; height: 897px; overflow: hidden; }
  body { background: var(--page); position: relative; font-family: "Roboto Condensed", Arial, sans-serif; color: var(--ink); }

  .card {
    position: absolute; top: 190px; width: 515px; height: 512px;
    background: radial-gradient(ellipse at 70% 75%, var(--card-light) 0%, var(--card) 70%);
    overflow: hidden;
  }
  .card::after {
    content: ""; position: absolute; left: 0; right: 0; bottom: 0; height: 7px; background: var(--accent);
  }
  .card--contact { left: 59px; }
  .card--brand { left: 626px; }

  .identity {
    position: absolute; right: 280px; top: 234px; text-align: right;
  }
  .identity__name {
    font-family: "Oswald", "Arial Narrow", sans-serif; font-weight: 500;
    font-size: 31px; line-height: 1; color: var(--accent); letter-spacing: 0.2px; white-space: nowrap;
  }
  .identity__role { font-size: 17px; line-height: 1; margin-top: 8px; }

  .divider { position: absolute; left: 253px; top: 236px; width: 1px; height: 54px; background: var(--ink); }

  .contacts { position: absolute; left: 274px; top: 230px; list-style: none; }
  .contacts li { display: flex; align-items: center; height: 21px; font-size: 17px; white-space: nowrap; }
  .contacts svg { width: 10px; height: 10px; margin-right: 9px; flex: none; }

  .address {
    position: absolute; left: 0; right: 0; top: 636px; top: 446px;
    text-align: center; font-size: 18px; white-space: nowrap;
  }

  .brand {
    position: absolute; left: 0; right: 0; top: 226px;
    display: flex; justify-content: center; align-items: center; gap: 12px;
  }
  .brand__dot { width: 12px; height: 12px; border-radius: 50%; background: var(--accent); }
  .brand__name { font-size: 52px; font-weight: 500; line-height: 1; color: var(--ink); letter-spacing: 1px; }
</style>
</head>
<body>
  <section class="card card--contact">
    <div class="identity">
      <h1 class="identity__name">WALEED RAFIQI</h1>
      <p class="identity__role">Managing Director</p>
    </div>
    <div class="divider"></div>
    <ul class="contacts">
      <li>
        <svg viewBox="0 0 10 10" aria-hidden="true"><path d="M2 0.8l1.6 0 .6 2-1 .9a5.5 5.5 0 0 0 2.2 2.4l.9-1 2 .6v1.6c-.4.6-1.4.9-2.2.6A8 8 0 0 1 1.3 3C1 2.2 1.3 1.2 2 .8z" fill="var(--accent)"/></svg>
        +971 50 317 6490
      </li>
      <li>
        <svg viewBox="0 0 10 10" aria-hidden="true"><rect x="0.6" y="2" width="8.8" height="6" fill="none" stroke="var(--accent)" stroke-width="1"/><path d="M0.8 2.3 5 5.4l4.2-3.1" fill="none" stroke="var(--accent)" stroke-width="1"/></svg>
        waleed@loomcrestuae.com
      </li>
      <li>
        <svg viewBox="0 0 10 10" aria-hidden="true"><g fill="none" stroke="var(--accent)" stroke-width="0.9"><circle cx="5" cy="5" r="4.3"/><ellipse cx="5" cy="5" rx="1.9" ry="4.3"/><path d="M0.7 5h8.6M1.4 2.8h7.2M1.4 7.2h7.2"/></g></svg>
        www.loomcrest.ae
      </li>
    </ul>
    <p class="address">Building C2 , Office 713 Dubai Saffron Heights</p>
  </section>

  <section class="card card--brand">
    <div class="brand">
      <span class="brand__dot"></span>
      <span class="brand__name">Loomcrest</span>
    </div>
  </section>
</body>
</html>
```